Holiday Rental Leaflet

Want a DL size double sided leaflet to distribute via local businesses, markets, family and friends
HOLIDAY RENTALCarrickalinga - 17 Brindle Street Sleeps 8-10 (2 Queen, 1 Double, 2 bunks), 4 bedrooms, BIR to all bedrooms 2 Bathrooms, one with bath, 2 toilets Open Plan Lounge/Dining/Kitchen area Dining Table for 8 peopleReverse cycle airconditionerSlow combustion wood heaterTV/DVD, CD/RadioKitchen has m/wave, oven, fridge/freezer, dishwasherBBQ providedTimber decking with 2 outside tables and 12 chairs Washing Machine and dryer provided One street back from beach Smoke free zone No Pets
For further information or to book contact Joan on 0491 287 306 or email joanfarrow27@velmarnet.com.au

Industry/Entity Type

Kitchen

Requirements
Nice to have
• Have sent a variety of photos of the house. No need to use all of them, pick out the most relevant for the leaflet.

```html
<!DOCTYPE html>
<html lang="en">
<head>
<meta charset="utf-8">
<title>Holiday Rental Leaflet – Carrickalinga</title>
<link rel="stylesheet" href="https://fonts.googleapis.com/css2?family=Oswald:wght@600;700&family=Roboto:wght@400;700&family=Roboto+Condensed:wght@400&family=Lobster&display=swap">
<style>
  :root{
    --stage:#4a4a4c;
    --white:#ffffff;
    --orange:#f4923a;
    --blue:#1a75bb;
    --ink:#2b2b2b;
    --rule:#9a9a9a;
    --yellow:#f3e623;
    --panel-blue:#bcd5ee;
    --icon:#333333;
  }
  *{box-sizing:border-box;margin:0;padding:0}
  html,body{width:1200px;height:844px;overflow:hidden;background:var(--stage)}
  .canvas{position:relative;width:1200px;height:844px;background:var(--stage);font-family:"Roboto",Arial,sans-serif;color:var(--ink)}
  .page{position:absolute;top:50px;width:528px;height:745px;overflow:hidden;box-shadow:6px 8px 14px rgba(0,0,0,.45)}
  .page--front{left:47px;background:linear-gradient(180deg,#6fc3ea 0%,#a9dcf3 28%,#3fb6d2 45%,#7fd1d9 60%,#e8e2cf 78%,#efe9d9 100%)}
  .page--back{left:626px;background:linear-gradient(180deg,#3da6e3 0%,#7fcbee 30%,#5fb7e2 60%,#8ea6dc 85%,#9aa2dc 100%)}
  .card{position:absolute;background:var(--white);box-shadow:0 6px 8px rgba(0,0,0,.28)}
  .photo{position:absolute}
  /* front */
  .title{position:absolute;left:0;right:0;top:12px;text-align:center;font-family:"Oswald",Impact,sans-serif;font-weight:700;font-size:60px;line-height:72px;color:var(--orange);letter-spacing:.5px}
  .title-rule{position:absolute;left:20px;right:30px;top:84px;height:1px;background:var(--rule)}
  .subtitle{position:absolute;left:0;right:0;top:91px;text-align:center;font-weight:700;font-size:19px;color:var(--blue);letter-spacing:.3px}
  .contact-lead{position:absolute;left:16px;top:10px;font-size:13px;letter-spacing:.4px}
  .contact-name{position:absolute;left:19px;top:36px;font-weight:700;font-size:17px;line-height:17px;color:var(--blue)}
  .contact-divider{position:absolute;left:96px;top:34px;width:1px;height:40px;background:var(--rule)}
  .contact-call{position:absolute;left:105px;top:28px;font-weight:700;font-size:23px;color:var(--blue);letter-spacing:.5px}
  .contact-email{position:absolute;left:105px;top:58px;font-weight:700;font-size:13px;color:var(--blue)}
  /* back */
  .features{position:absolute;left:261px;top:28px;width:190px;list-style:none;font-family:"Roboto Condensed",Arial,sans-serif;font-size:12px;line-height:15px;color:var(--ink)}
  .feature{position:absolute;left:0;width:190px;white-space:nowrap}
  .feature svg{position:absolute;left:-38px;top:0;width:30px;height:24px;fill:none;stroke:var(--icon);stroke-width:1.4;stroke-linecap:round;stroke-linejoin:round}
  .feature--pair-divider{position:absolute;left:95px;width:1px;height:24px;background:var(--rule)}
  .tagline{position:absolute;left:0;right:0;top:508px;text-align:center;font-family:"Lobster",cursive;font-size:21px;color:var(--yellow)}
  .reach-panel{position:absolute;left:12px;top:11px;width:436px;height:150px;background:var(--panel-blue)}
  .map{position:absolute;left:168px;top:0;width:268px;height:150px;background:linear-gradient(135deg,#e9e7e1,#dcdad4);clip-path:polygon(22% 0,100% 0,100% 100%,0 100%)}
  .reach-name{position:absolute;left:12px;top:12px;font-weight:700;font-size:17px;color:var(--blue);letter-spacing:.3px}
  .reach-call{position:absolute;left:12px;top:34px;font-weight:700;font-size:15px;color:var(--blue);letter-spacing:.4px}
  .reach-email{position:absolute;left:12px;top:53px;font-weight:700;font-size:12px;color:var(--blue)}
  .reach-heading{position:absolute;left:12px;top:110px;font-weight:700;font-size:14px;color:var(--ink)}
  .reach-address{position:absolute;left:12px;top:129px;font-size:13px;color:var(--ink)}
</style>
</head>
<body>
<div class="canvas">

  <section class="page page--front" role="img" aria-label="Tropical beach backdrop with palm leaves, turquoise sea and sand">
    <header class="card" style="left:35px;top:45px;width:459px;height:125px">
      <h1 class="title">HOLIDAY RENTAL</h1>
      <div class="title-rule"></div>
      <p class="subtitle">CARRICKALINGA - 17 BRINDLE STREET</p>
    </header>

    <div class="card" style="left:35px;top:207px;width:459px;height:381px">
      <div class="photo" style="left:11px;top:16px;width:436px;height:208px;background:linear-gradient(180deg,#b9d4ea 0%,#9aa9a8 35%,#8c7a55 60%,#7e8a5a 85%,#a89d7b 100%)" role="img" aria-label="Photo of the timber beach house on stilts with a wraparound deck"></div>
      <div class="photo" style="left:11px;top:236px;width:213px;height:133px;background:linear-gradient(180deg,#b97a3c 0%,#c88b4c 45%,#2d3a66 75%,#a87a4e 100%)" role="img" aria-label="Photo of the timber-lined lounge with navy sofas"></div>
      <div class="photo" style="left:237px;top:236px;width:209px;height:133px;background:linear-gradient(180deg,#d0c2b0 0%,#ece9e4 45%,#6f6258 70%,#f2f2f0 100%)" role="img" aria-label="Photo of the white kitchen with island bench"></div>
    </div>

    <div class="photo" style="left:386px;top:598px;width:120px;height:120px;border-radius:50%;background:radial-gradient(circle,#d9b377 0%,rgba(217,179,119,.6) 50%,rgba(217,179,119,0) 72%)" role="img" aria-label="Starfish on the sand"></div>

    <footer class="card" style="left:35px;top:628px;width:459px;height:87px">
      <p class="contact-lead">FOR FURTHER INFORMATION OR TO BOOK CONTACT</p>
      <p class="contact-name">JOAN<br>FARROW</p>
      <div class="contact-divider"></div>
      <p class="contact-call">CALL : 0491 287 306</p>
      <p class="contact-email">email: joanfarrow27@velmarnet.com.au</p>
    </footer>
  </section>

  <section class="page page--back" role="img" aria-label="Blue ocean backdrop with palm leaves">
    <div class="card" style="left:34px;top:66px;width:459px;height:432px">
      <div class="photo" style="left:15px;top:18px;width:188px;height:124px;background:linear-gradient(180deg,#cfe2f1 0%,#7fa8cc 30%,#3f6f9e 50%,#6f7f5a 75%,#8c8a70 100%)" role="img" aria-label="Photo of the sea view over the garden"></div>
      <div class="photo" style="left:15px;top:156px;width:188px;height:124px;background:linear-gradient(180deg,#e7dccb 0%,#c99a5f 40%,#6f8fa8 70%,#b7a48c 100%)" role="img" aria-label="Photo of the bunk room with two sets of bunks"></div>
      <div class="photo" style="left:15px;top:294px;width:188px;height:122px;background:linear-gradient(180deg,#c98d4c 0%,#b7773a 40%,#5c7f95 70%,#8aa5b0 100%)" role="img" aria-label="Photo of the queen bedroom with striped bedding"></div>

      <ul class="features">
        <li class="feature" style="top:0">
          <svg viewBox="0 0 30 24"><rect x="3" y="6" width="24" height="12"/><rect x="6" y="8" width="7" height="4"/><line x1="3" y1="18" x2="3" y2="21"/><line x1="27" y1="18" x2="27" y2="21"/></svg>
          SLEEPS 8-10<br>(2 Queen, 1 Double, 2 bunks),
        </li>
        <li class="feature" style="top:44px">
          <svg viewBox="0 0 30 24"><rect x="3" y="8" width="24" height="9"/><rect x="6" y="5" width="8" height="4"/><rect x="16" y="5" width="8" height="4"/><line x1="4" y1="17" x2="4" y2="20"/><line x1="26" y1="17" x2="26" y2="20"/></svg>
          4 Bedrooms, BIR to all bedrooms
        </li>
        <li class="feature" style="top:74px">
          <svg viewBox="0 0 30 24"><path d="M4 11h22v3a5 5 0 0 1-5 5H9a5 5 0 0 1-5-5z"/><path d="M7 11V5a2 2 0 0 1 4 0"/><line x1="9" y1="19" x2="8" y2="21"/><line x1="21" y1="19" x2="22" y2="21"/></svg>
          2 Bathrooms, one with bath,
        </li>
        <li class="feature" style="top:104px">
          <svg viewBox="0 0 30 24"><path d="M9 3h12v5H9z"/><path d="M8 8h14l-2 6h-10z"/><path d="M12 14v7h6v-7"/></svg>
          2 Toilets
        </li>
        <li class="feature" style="top:134px">
          <svg viewBox="0 0 30 24"><circle cx="15" cy="13" r="7"/><circle cx="15" cy="13" r="4"/><line x1="4" y1="5" x2="4" y2="21"/><path d="M2 5v4a2 2 0 0 0 4 0V5"/><path d="M26 21V5c-2 1-2 6 0 8"/></svg>
          Open Plan Lounge/Dining/Kitchen area<br>Dining Table for 8 people Reverse cycle
        </li>
        <li class="feature" style="top:178px">
          <svg viewBox="0 0 30 24"><rect x="2" y="4" width="26" height="9"/><line x1="5" y1="10" x2="25" y2="10"/><path d="M7 16v3M12 16v3M18 16v3M23 16v3"/></svg>
          Airconditioner Slow combustion<br>wood heater TV/DVD, CD/Radio
        </li>
        <li class="feature" style="top:222px">
          <svg viewBox="0 0 30 24"><rect x="3" y="4" width="24" height="16" rx="2"/><rect x="6" y="7" width="13" height="10"/><line x1="23" y1="8" x2="23" y2="9"/><line x1="23" y1="12" x2="23" y2="13"/></svg>
          Kitchen has m/wave, oven, fridge/<br>freezer, dishwasher
        </li>
        <li class="feature" style="top:267px">
          <svg viewBox="0 0 30 24"><path d="M5 9h20a10 7 0 0 1-20 0z"/><line x1="10" y1="15" x2="7" y2="22"/><line x1="20" y1="15" x2="23" y2="22"/><path d="M11 2c-1 2 1 3 0 5M15 2c-1 2 1 3 0 5M19 2c-1 2 1 3 0 5"/></svg>
          BBQ provided Timber decking with 2<br>outside tables and 12 chairs
        </li>
        <li class="feature" style="top:311px">
          <svg viewBox="0 0 30 24"><rect x="5" y="2" width="20" height="20"/><line x1="5" y1="6" x2="25" y2="6"/><circle cx="15" cy="14" r="5"/><circle cx="15" cy="14" r="2"/></svg>
          Washing Machine and dryer provided
        </li>
        <li class="feature" style="top:341px">
          <svg viewBox="0 0 30 24"><path d="M4 10a11 8 0 0 1 20-3z"/><line x1="14" y1="8" x2="19" y2="20"/><line x1="4" y1="21" x2="27" y2="21"/><path d="M20 18h6"/></svg>
          One street back from beach
        </li>
        <li class="feature" style="top:369px;width:90px">
          <svg viewBox="0 0 30 24"><circle cx="15" cy="12" r="9"/><line x1="9" y1="6" x2="21" y2="18"/><rect x="9" y="11" width="10" height="3"/></svg>
          Smoke free zone
        </li>
        <li class="feature--pair-divider" style="top:364px"></li>
        <li class="feature" style="top:369px;left:138px;width:52px">
          <svg viewBox="0 0 30 24"><circle cx="15" cy="12" r="9"/><line x1="9" y1="6" x2="21" y2="18"/></svg>
          No Pets
        </li>
      </ul>
    </div>

    <p class="tagline">Enjoy the summer with us.....</p>

    <div class="card" style="left:34px;top:543px;width:459px;height:170px">
      <div class="reach-panel">
        <div class="map" role="img" aria-label="Street map of Carrickalinga with a pin at 17 Brindle Street"></div>
        <p class="reach-name">JOAN FARROW</p>
        <p class="reach-call">CALL : 0491 287 306</p>
        <p class="reach-email">email: joanfarrow27@velmarnet.com.au</p>
        <p class="reach-heading">HOW TO REACH</p>
        <p class="reach-address">Carrickalinga - 17 Brindle Street</p>
      </div>
    </div>
  </section>

</div>
</body>
</html>
```